Tarvel Ridge LLC

Need Professional Business cards for New Investment Fund

Target Market(s)

High Quality investors

Industry/Entity Type

Financial

Contact Information for Business Card

Phone Number +1 555 284 6193
Name Pavel Orlinsky
Title Fund Manager
email po@FundTarvel.example
Website www.FundTarvel.example

Colors

Designer to choose colors to be used in the design.

Requirements
Must have
• Must have our Logo and all of the above. Must be made so lettering and loge can be raised

```html
<!DOCTYPE html>
<html lang="en">
<head>
<meta charset="utf-8">
<title>Tarvel Ridge LLC – Business Card</title>
<link rel="stylesheet" href="https://fonts.googleapis.com/css2?family=Roboto:wght@400;500;700&display=swap">
<style>
  :root {
    --page-bg: #e4e4e4;
    --card-white: #ffffff;
    --card-dark: #2a2a2a;
    --card-dark-2: #3c3c3c;
    --accent-green: #19e619;
    --text-grey: #5a5a5a;
    --divider-grey: #c4c4c4;
  }
  * { box-sizing: border-box; margin: 0; padding: 0; }
  html, body {
    width: 1200px; height: 801px; overflow: hidden;
    background: var(--page-bg);
    font-family: "Roboto", Arial, sans-serif;
  }
  .sheet {
    position: relative; width: 1200px; height: 801px;
    display: flex; align-items: center; justify-content: center; gap: 48px;
  }
  .card {
    position: relative; width: 525px; height: 300px;
    border-right: 3px solid var(--accent-green);
    border-bottom: 3px solid var(--accent-green);
    box-shadow: 0 10px 24px rgba(0,0,0,0.18);
  }
  .card-front {
    background: var(--card-white);
    display: flex; align-items: center;
  }
  .brand {
    width: 230px; display: flex; align-items: center; justify-content: center; gap: 10px;
  }
  .brand-square {
    width: 16px; height: 16px; background: var(--accent-green);
  }
  .brand-name {
    font-size: 22px; font-weight: 700; color: var(--accent-green); letter-spacing: 0.5px;
  }
  .divider {
    width: 1px; height: 110px; background: var(--divider-grey);
  }
  .contact { padding-left: 22px; }
  .contact-name {
    font-size: 22px; font-weight: 700; color: var(--accent-green); line-height: 1.1;
  }
  .contact-title {
    font-size: 14px; font-weight: 500; color: var(--text-grey); margin: 3px 0 12px;
  }
  .contact-list { list-style: none; }
  .contact-list li {
    display: flex; align-items: center; gap: 8px;
    font-size: 13.5px; color: var(--text-grey); line-height: 1.55;
  }
  .contact-list svg { width: 11px; height: 11px; flex: none; }
  .card-back {
    background: linear-gradient(135deg, var(--card-dark-2), var(--card-dark));
    overflow: hidden;
  }
  .back-texture {
    position: absolute; inset: 0;
    background: linear-gradient(120deg, rgba(255,255,255,0.06), rgba(255,255,255,0) 55%, rgba(0,0,0,0.25));
  }
  .back-brand {
    position: absolute; right: 30px; bottom: 30px;
    display: flex; align-items: center; gap: 7px;
  }
  .back-brand .brand-square { width: 10px; height: 10px; }
  .back-brand .brand-name { font-size: 14px; color: var(--card-white); }
</style>
</head>
<body>
<main class="sheet">
  <section class="card card-front">
    <div class="brand">
      <span class="brand-square"></span>
      <span class="brand-name">Tarvel Ridge</span>
    </div>
    <div class="divider"></div>
    <div class="contact">
      <p class="contact-name">Pavel Orlinsky</p>
      <p class="contact-title">Fund Manager</p>
      <ul class="contact-list">
        <li>
          <svg viewBox="0 0 12 12"><path d="M2.5 1h2l1 3-1.4 1a6 6 0 0 0 3 3l1-1.4 3 1v2a1 1 0 0 1-1 1A9.5 9.5 0 0 1 1.5 2a1 1 0 0 1 1-1z" fill="var(--accent-green)"/></svg>
          +1 555 284 6193
        </li>
        <li>
          <svg viewBox="0 0 12 12"><rect x="0.5" y="2" width="11" height="8" rx="1" fill="var(--accent-green)"/><path d="M1 2.8 6 6.5l5-3.7" stroke="#fff" stroke-width="1" fill="none"/></svg>
          po@FundTarvel.example
        </li>
        <li>
          <svg viewBox="0 0 12 12"><circle cx="6" cy="6" r="5.5" fill="var(--accent-green)"/><path d="M0.8 6h10.4M6 0.8c-2.4 3-2.4 7.4 0 10.4M6 0.8c2.4 3 2.4 7.4 0 10.4" stroke="#fff" stroke-width="0.8" fill="none"/></svg>
          www.FundTarvel.example
        </li>
      </ul>
    </div>
  </section>

  <section class="card card-back">
    <div class="back-texture" role="img" aria-label="Dark embossed repeating brand pattern across the card back"></div>
    <div class="back-brand">
      <span class="brand-square"></span>
      <span class="brand-name">Tarvel Ridge</span>
    </div>
  </section>
</main>
</body>
</html>
```